Business Card and Letterhead for new company Vardel GreenWorks, Inc.

Vardel GreenWorks, Inc., an engineering and construction firm that provides services for solid waste landfill gas systems, needs a business card and letterhead. We recently had a logo designed but we are open to some tweaks to logo design and color scheme. Generally, we like "earthy" color tones - greens, browns, oranges. This is a sister company - www.talvoriengineering.example.

Target Market(s)

Solid waste landfill companies - Brindle Disposal, Halcott Hauling, etc.

Industry/Entity Type

Engineering and Construction

Contact Information for Business Card

Name, Title, email, mobile phone, work phone, website. Potential list of services for back of card: LFG Engineering and Design, GCCS Planning and Operational Consulting, Compliance Monitoring and Reporting, Routine Operations & Maintenance, Nonroutine O&M, Construction Management, Construction QA, GCCS Construction

Font styles to use
Sans Serif

Requirements
Must have
• Logo, pertinent information, maybe a tagline (still in development)
Nice to have
• For back of card, considering an engineering scale (attached for another business of ours), but want to look at other options, alternatives. Like the idea of the back of card to have some utility (scale, unit conversion info, list of services) but willing to consider lots of options.
Should not have
• Needs to have a professional (engineering) and technical look, not cartoonish.

```html
<!DOCTYPE html>
<html lang="en">
<head>
<meta charset="utf-8">
<title>Vardel GreenWorks, Inc. — Business Card</title>
<link href="https://fonts.googleapis.com/css2?family=Roboto:wght@400;700;900&display=swap" rel="stylesheet">
<style>
  :root {
    --stage: #2b2c2e;
    --teal-deep: #1c7fa0;
    --teal-bright: #2cc0d4;
    --teal-mid: #2192b2;
    --brand-green: #6aae2e;
    --brand-blue: #2a8fb4;
    --ink: #3c3c3c;
    --rule: #c9c9c9;
    --paper: #ffffff;
    --white: #ffffff;
  }
  * { box-sizing: border-box; margin: 0; padding: 0; }
  html, body { width: 1200px; height: 874px; overflow: hidden; }
  body {
    background: var(--stage);
    font-family: "Roboto", Arial, sans-serif;
    position: relative;
  }
  .card {
    position: absolute;
    width: 665px;
    height: 380px;
    border-radius: 22px;
    overflow: hidden;
  }

  /* ---------- back of card ---------- */
  .card-back {
    left: 420px;
    top: 40px;
    background: var(--teal-mid);
    color: var(--white);
  }
  .back-pattern {
    position: absolute;
    inset: 0;
    background: linear-gradient(125deg, var(--teal-deep) 0%, var(--teal-mid) 50%, var(--teal-bright) 100%);
    opacity: 0.9;
  }
  .back-content {
    position: absolute;
    inset: 0;
    display: flex;
    flex-direction: column;
    align-items: center;
    justify-content: center;
    gap: 26px;
  }
  .back-brand {
    display: flex;
    align-items: center;
    gap: 10px;
    font-weight: 700;
    font-size: 26px;
    letter-spacing: 0.5px;
  }
  .back-brand .brand-dot {
    width: 18px; height: 18px; border-radius: 50%;
    background: var(--white);
  }
  .services {
    list-style: none;
    text-align: center;
    font-size: 15.5px;
    line-height: 1.55;
  }
  .services .sep { color: var(--teal-bright); padding: 0 6px; }

  /* ---------- front of card ---------- */
  .card-front {
    left: 135px;
    top: 454px;
    background: var(--paper);
    color: var(--ink);
  }
  .front-watermark {
    position: absolute;
    left: 40px; top: 30px;
    width: 230px; height: 280px;
    border-radius: 50%;
    background: radial-gradient(circle, rgba(106,174,46,0.07) 0%, rgba(42,143,180,0.05) 55%, rgba(255,255,255,0) 75%);
  }
  .front-brand {
    position: absolute;
    left: 330px; top: 92px;
    display: flex;
    align-items: center;
    gap: 12px;
    color: var(--brand-green);
    font-weight: 700;
    font-size: 27px;
  }
  .front-brand .brand-dot {
    width: 26px; height: 26px; border-radius: 50%;
    background: var(--brand-blue);
  }
  .person {
    position: absolute;
    left: 56px; top: 160px;
  }
  .person-name {
    color: var(--brand-green);
    font-weight: 900;
    font-size: 27px;
    letter-spacing: 1.5px;
  }
  .person-title {
    color: var(--brand-blue);
    font-size: 15px;
    margin-top: 2px;
  }
  .contacts {
    position: absolute;
    left: 56px; top: 232px;
    list-style: none;
    font-size: 16px;
    line-height: 23px;
  }
  .contacts li { display: flex; align-items: center; gap: 10px; }
  .contacts svg { width: 14px; height: 14px; flex: none; }
  .divider {
    position: absolute;
    left: 56px; right: 40px; top: 222px;
    height: 1px;
    background: var(--rule);
  }
  .address {
    position: absolute;
    right: 40px; top: 228px;
    text-align: right;
    font-size: 16px;
    line-height: 22px;
  }
  .address .company {
    display: block;
    padding-bottom: 4px;
    margin-bottom: 4px;
    border-bottom: 1px solid var(--rule);
  }
  .band {
    position: absolute;
    left: 0; right: 0; bottom: 0;
    height: 16px;
    display: flex;
  }
  .band-green { flex: 0 0 62%; background: var(--brand-green); }
  .band-gap { flex: 0 0 4px; background: var(--paper); }
  .band-blue { flex: 1; background: var(--brand-blue); }
</style>
</head>
<body>

  <section class="card card-back">
    <div class="back-pattern" role="img" aria-label="Repeating embossed pattern of the company mark in teal tones"></div>
    <div class="back-content">
      <div class="back-brand"><span class="brand-dot"></span>Vardel GreenWorks, Inc.</div>
      <ul class="services">
        <li>LFG Engineering &amp; Design<span class="sep">•</span>GCCS Planning &amp; Operational Consulting</li>
        <li>Compliance Monitoring &amp; Reporting<span class="sep">•</span>Routine Operations &amp; Maintenance</li>
        <li>Nonroutine O&amp;M, Construction Management<span class="sep">•</span>Construction QA, GCCS Construction</li>
      </ul>
    </div>
  </section>

  <section class="card card-front">
    <div class="front-watermark" role="img" aria-label="Faint oversized company mark in the background"></div>

    <div class="front-brand"><span class="brand-dot"></span>Vardel GreenWorks, Inc.</div>

    <div class="person">
      <div class="person-name">DANIEL ORTMAN</div>
      <div class="person-title">President</div>
    </div>

    <div class="divider"></div>

    <ul class="contacts">
      <li>
        <svg viewBox="0 0 16 16"><path d="M4 1l2.5 3-1.5 2c1 2 3 4 5 5l2-1.5 3 2.5-2 2.5C7 14 2 9 1.5 3.5z" fill="var(--brand-green)"/></svg>
        555-014-2066
      </li>
      <li>
        <svg viewBox="0 0 16 16"><rect x="4" y="1" width="8" height="14" rx="1.5" fill="none" stroke="var(--brand-green)" stroke-width="1.6"/><circle cx="8" cy="12.5" r="0.9" fill="var(--brand-green)"/></svg>
        555-014-2067
      </li>
      <li>
        <svg viewBox="0 0 16 16"><rect x="1" y="3" width="14" height="10" rx="1" fill="var(--brand-green)"/><path d="M1.5 3.5L8 9l6.5-5.5" fill="none" stroke="#fff" stroke-width="1.3"/></svg>
        info@talvoriengineering.example
      </li>
      <li>
        <svg viewBox="0 0 16 16"><circle cx="8" cy="8" r="7" fill="var(--brand-green)"/><path d="M1 8h14M8 1c-3 3-3 11 0 14M8 1c3 3 3 11 0 14" fill="none" stroke="#fff" stroke-width="1"/></svg>
        www.talvoriengineering.example
      </li>
    </ul>

    <address class="address" style="font-style:normal">
      <span class="company">Talvori Engineering, LLC</span>
      4800 Ridgeback Lane<br>
      Suite 210, Marlow Falls, TN<br>
      37999, United States
    </address>

    <div class="band">
      <div class="band-green"></div>
      <div class="band-gap"></div>
      <div class="band-blue"></div>
    </div>
  </section>

</body>
</html>
```